Modernise Business Card

Our company has been operating for 10 years. With the start of the new decade we are looking to refresh our business card design. We manufacture a range of industrial product shipping to customers internationally. A copy of our current card, both sides, is attached. We are looking for a mature professional appearance.

```html
<!DOCTYPE html>
<html lang="en">
<head>
<meta charset="utf-8">
<title>Norvex Business Card</title>
<link href="https://fonts.googleapis.com/css2?family=PT+Sans+Narrow:wght@400;700&family=PT+Sans:wght@700&display=swap" rel="stylesheet">
<style>
  :root {
    --canvas: #e9e7e4;
    --card-dark: #050505;
    --card-light: #f7f7f8;
    --ink: #1e1e1e;
    --brand-blue: #1c92c3;
    --bar-grey: #333333;
    --white: #ffffff;
  }
  * { margin: 0; padding: 0; box-sizing: border-box; }
  html, body {
    width: 1200px; height: 1200px; overflow: hidden;
    background: var(--canvas);
  }
  .canvas {
    width: 1200px; height: 1200px;
    display: flex; flex-direction: column; align-items: center; justify-content: center;
    gap: 60px;
  }
  .card {
    width: 880px; height: 500px; position: relative; overflow: hidden;
    box-shadow: 0 10px 30px rgba(0,0,0,0.18);
  }

  /* Front side */
  .card-front { background: var(--card-dark); color: var(--white); }
  .front-brand {
    position: absolute; left: 190px; top: 150px;
    font-family: "PT Sans Narrow", sans-serif; font-weight: 700;
    font-size: 150px; line-height: 1; color: var(--white); letter-spacing: 2px;
  }
  .front-services {
    position: absolute; left: 196px; top: 330px;
    display: flex; gap: 34px;
    font-family: "PT Sans Narrow", sans-serif; font-size: 28px; color: var(--white);
  }

  /* Back side */
  .card-back { background: var(--card-light); color: var(--ink); font-family: "PT Sans Narrow", sans-serif; }
  .edge-bar { position: absolute; width: 22px; background: var(--bar-grey); }
  .edge-bar.left { left: 0; top: 110px; height: 240px; }
  .edge-bar.right { right: 0; top: 180px; height: 260px; }
  .back-brand {
    position: absolute; left: 110px; top: 150px;
    font-family: "PT Sans Narrow", sans-serif; font-weight: 700;
    font-size: 110px; line-height: 1; color: var(--brand-blue); letter-spacing: 1px;
  }
  .divider { position: absolute; left: 470px; top: 40px; width: 2px; height: 340px; background: var(--ink); }
  .contact { position: absolute; left: 500px; top: 42px; }
  .person-name {
    font-family: "PT Sans", sans-serif; font-weight: 700;
    font-size: 44px; color: var(--brand-blue); line-height: 1.05;
  }
  .person-title { font-size: 28px; line-height: 1.1; margin-bottom: 24px; }
  .row { display: flex; align-items: flex-start; gap: 12px; font-size: 30px; line-height: 1.3; margin-bottom: 10px; }
  .row svg { width: 26px; height: 26px; flex: none; margin-top: 7px; }
  .phones { display: grid; grid-template-columns: 100px auto; }
  .address {
    position: absolute; left: 50px; bottom: 40px;
    display: flex; align-items: center; gap: 14px; font-size: 27px;
  }
  .address svg { width: 20px; height: 28px; }
</style>
</head>
<body>
<main class="canvas">
  <section class="card card-front">
    <div class="front-brand">Norvex</div>
    <div class="front-services">
      <span>Hydraulic Adapters</span>
      <span>Hose Fittings</span>
      <span>Quick Couplings</span>
    </div>
  </section>

  <section class="card card-back">
    <div class="edge-bar left"></div>
    <div class="edge-bar right"></div>
    <div class="back-brand">Norvex</div>
    <div class="divider"></div>
    <div class="contact">
      <div class="person-name">Alan Brooks</div>
      <div class="person-title">Managing Director</div>
      <div class="row">
        <svg viewBox="0 0 24 24" aria-hidden="true"><path d="M6.6 10.8a15 15 0 0 0 6.6 6.6l2.2-2.2a1 1 0 0 1 1-.25 11.4 11.4 0 0 0 3.6.57 1 1 0 0 1 1 1V20a1 1 0 0 1-1 1A17 17 0 0 1 3 4a1 1 0 0 1 1-1h3.5a1 1 0 0 1 1 1c0 1.25.2 2.45.57 3.6a1 1 0 0 1-.25 1z" fill="none" stroke="var(--brand-blue)" stroke-width="2"/></svg>
        <div class="phones">
          <span>China</span><span>+86 150 2233 0417</span>
          <span>Australia</span><span>+61 412 508 731</span>
        </div>
      </div>
      <div class="row">
        <svg viewBox="0 0 24 24" aria-hidden="true"><rect x="2" y="4" width="20" height="16" fill="none" stroke="var(--brand-blue)" stroke-width="2.5"/><path d="M2 5l10 8 10-8" fill="none" stroke="var(--brand-blue)" stroke-width="2.5"/></svg>
        <span>abrooks@norvexfittings.com</span>
      </div>
      <div class="row">
        <svg viewBox="0 0 24 24" aria-hidden="true"><circle cx="12" cy="12" r="10" fill="var(--brand-blue)"/><path d="M2 12h20M12 2v20M5 6h14M5 18h14" stroke="var(--white)" stroke-width="1.2" fill="none"/><ellipse cx="12" cy="12" rx="4.5" ry="10" fill="none" stroke="var(--white)" stroke-width="1.2"/></svg>
        <span>www.norvexfittings.com</span>
      </div>
    </div>
    <div class="address">
      <svg viewBox="0 0 20 28" aria-hidden="true"><path d="M10 1a8.5 8.5 0 0 0-8.5 8.5C1.5 16 10 27 10 27s8.5-11 8.5-17.5A8.5 8.5 0 0 0 10 1z" fill="var(--brand-blue)"/><circle cx="10" cy="9.5" r="3.2" fill="var(--card-light)"/></svg>
      <span>1208-3, Lanting Building 416 Qiaoxin Road, Haishu District Ningbo 315010 China</span>
    </div>
  </section>
</main>
</body>
</html>
```